Business card for a young aspring actress

My daughter is 18 and just starting out on her profession as an actress. She is a member of the Harbour Young Players and has already had some extras work and a featured role in an upcoming Feature film.

She wants/needs a card that she can have to hand to give to those she comes into contact with in the theatre, TV and film industries.

We are thinking that it may be double sided with an impact side including a picture of her and her name etc with the reverse holding contact and other details.

She wants to go by the name Maya Louise Brennick.

She has done a little modelling but sees herself as an actress.

She can be seen in this video
http://www.oakvalepark-academy.org/videos/be0881e4276ee2512c50a07f907c1d03?width=640&height=480

Target Market(s)

Anyone she comes into contact with in theatre TV and film industries.

Industry/Entity Type

Business

Requirements
Nice to have
• She has email and a website www.mayabrennick.com She is quite a connected girl

```html
<!DOCTYPE html>
<html lang="en">
<head>
<meta charset="utf-8">
<title>Maya Louise Brennick – Business Card</title>
<link rel="stylesheet" href="https://fonts.googleapis.com/css2?family=Open+Sans:ital,wght@0,400;0,600;0,700;1,400&display=swap">
<style>
  :root {
    --stage-top: #6a5a9c;
    --stage-bottom: #2a1a8a;
    --card-white: #ffffff;
    --ink: #111111;
    --band-black: #0d0d0d;
    --strip-light: rgba(236, 232, 224, 0.85);
    --wall-pale: #b9b79a;
    --room-dark: #1e120c;
    --hair-brown: #5a3520;
    --skin-warm: #e0a68a;
    --blazer-beige: #d2c9b4;
    --top-white: #f4f2ee;
    --gold: #a98a4a;
    --grey-bright: #f2f2f2;
    --grey-soft: #d8d8d8;
    --grey-mid: #9a9a9a;
    --grey-deep: #2e2e2e;
  }
  * { box-sizing: border-box; margin: 0; padding: 0; }
  html, body {
    width: 1200px; height: 857px; overflow: hidden;
    background: linear-gradient(160deg, var(--stage-top), var(--stage-bottom));
    font-family: "Open Sans", Verdana, sans-serif;
  }
  .card {
    position: absolute; top: 78px;
    width: 440px; height: 700px;
    overflow: hidden;
    box-shadow: 0 12px 30px rgba(0,0,0,0.45);
  }
  .card--front { left: 130px; }
  .card--back { left: 630px; background: var(--card-white); }

  .front-photo {
    position: absolute; inset: 0;
    background:
      radial-gradient(ellipse 28% 22% at 44% 30%, var(--skin-warm) 0%, rgba(224,166,138,0.6) 55%, rgba(224,166,138,0) 100%),
      radial-gradient(ellipse 22% 14% at 42% 60%, rgba(169,138,74,0.9) 0%, rgba(169,138,74,0) 100%),
      radial-gradient(ellipse 16% 20% at 40% 92%, var(--top-white) 0%, rgba(244,242,238,0) 100%),
      radial-gradient(ellipse 55% 30% at 55% 88%, var(--blazer-beige) 0%, rgba(210,201,180,0.7) 60%, rgba(210,201,180,0) 100%),
      radial-gradient(ellipse 40% 38% at 45% 34%, var(--hair-brown) 0%, rgba(90,53,32,0.6) 60%, rgba(90,53,32,0) 100%),
      radial-gradient(ellipse 22% 45% at 5% 35%, var(--wall-pale) 0%, rgba(185,183,154,0.5) 60%, rgba(185,183,154,0) 100%),
      linear-gradient(180deg, #2b1c14 0%, var(--room-dark) 100%);
  }
  .front-strip {
    position: absolute; left: 108px; right: 0; bottom: 38px;
    padding: 8px 12px 6px 12px;
    background: var(--strip-light);
    text-align: right;
  }
  .front-name {
    font-size: 27px; font-weight: 400; color: var(--ink);
    line-height: 1.1; white-space: nowrap;
  }
  .front-disciplines {
    font-size: 11.5px; letter-spacing: 2.8px; color: var(--ink);
    margin-top: 3px; white-space: nowrap;
  }

  .back-art { position: absolute; inset: 0; }
  .back-identity { position: absolute; left: 26px; top: 462px; }
  .back-name { font-size: 23px; font-weight: 700; color: var(--ink); line-height: 1.1; }
  .back-role { font-size: 10px; letter-spacing: 1.4px; color: var(--ink); }
  .back-contact { position: absolute; left: 26px; top: 526px; color: var(--ink); }
  .back-agent { font-size: 16.5px; font-weight: 700; margin-bottom: 3px; }
  .back-agent em { font-weight: 400; }
  .contact-line { font-size: 13px; line-height: 19px; }
  .contact-line b { font-weight: 700; }
  .contact-line i { font-style: italic; }
</style>
</head>
<body>
  <section class="card card--front">
    <div class="front-photo" role="img" aria-label="Colour portrait of the actress smiling, long brown hair, light beige blazer over a white top and a gold statement necklace, patterned wallpaper behind"></div>
    <div class="front-strip">
      <div class="front-name">Maya Louise Brennick</div>
      <div class="front-disciplines">MODELLING • FILM • TV • THEATRE</div>
    </div>
  </section>

  <section class="card card--back">
    <svg class="back-art" width="440" height="700" viewBox="0 0 440 700">
      <defs>
        <linearGradient id="greyBase" x1="0" y1="0" x2="1" y2="0">
          <stop offset="0" stop-color="var(--grey-soft)"/>
          <stop offset="0.2" stop-color="var(--grey-deep)"/>
          <stop offset="0.5" stop-color="var(--grey-bright)"/>
          <stop offset="0.82" stop-color="var(--grey-mid)"/>
          <stop offset="1" stop-color="var(--grey-soft)"/>
        </linearGradient>
        <radialGradient id="greyLight" cx="0.52" cy="0.55" r="0.4">
          <stop offset="0" stop-color="var(--grey-bright)" stop-opacity="0.95"/>
          <stop offset="1" stop-color="var(--grey-bright)" stop-opacity="0"/>
        </radialGradient>
      </defs>
      <g role="img" aria-label="Black and white close-up headshot of the actress with long straight hair, hand resting at her cheek">
        <polygon points="0,0 418,0 418,458 0,436" fill="url(#greyBase)"/>
        <polygon points="0,0 418,0 418,458 0,436" fill="url(#greyLight)"/>
      </g>
      <polygon points="0,436 440,459 440,471 0,448" fill="var(--band-black)"/>
    </svg>
    <div class="back-identity">
      <div class="back-name">Maya Louise Brennick</div>
      <div class="back-role">Actress</div>
    </div>
    <div class="back-contact">
      <div class="back-agent">Represented by <em>xxxxxxxxxx</em></div>
      <div class="contact-line"><b>Microblog:</b> <i>xxxxxx</i></div>
      <div class="contact-line"><b>Profile:</b> <i>xxxxxx</i></div>
      <div class="contact-line"><b>Email:</b> <i>xxx@mayabrennick.com</i></div>
      <div class="contact-line"><b>Website:</b> www.mayabrennick.com</div>
      <div class="contact-line"><b>Tel:</b> 00000 00000000</div>
    </div>
  </section>
</body>
</html>
```